Crestway screen porch

Can you please design a flyer for me promoting my screen porch businessPlease remove the seamless gutters word from the title and add “screen porches” I have added the logo and a bunch of pictures from projects that I have done in the past. You can use words like Hillcrest Screen porches, etc

Target Market(s)

homeowners, contractors, builders

Industry/Entity Type

Construction

Requirements
Must have
• Dom Karsten
• Crestway Gutters
• 2957 Old Hwy 38 N, Greer, SC 29873
• 864-555-0186
Nice to have
• A few colors maybe 3 most
• nice looking font

```html
<!DOCTYPE html>
<html lang="en">
<head>
<meta charset="utf-8">
<title>Crestway Screen Porches Flyer</title>
<link href="https://fonts.googleapis.com/css2?family=Bebas+Neue&family=Montserrat:wght@400;600;700;800&display=swap" rel="stylesheet">
<style>
  :root{
    --red:#d9172f;
    --dark:#2e2e30;
    --ink:#3a3a3c;
    --white:#ffffff;
    --stage:#dcdcde;
    --muted:#5a5a5c;
  }
  *{box-sizing:border-box;margin:0;padding:0}
  html,body{width:1200px;height:986px;overflow:hidden;background:var(--stage)}
  .flyer{position:absolute;left:250px;top:13px;width:700px;height:960px;background:var(--white);overflow:hidden;box-shadow:0 6px 22px rgba(0,0,0,.18);font-family:'Montserrat',sans-serif;color:var(--ink)}
  .hero{position:absolute;left:0;top:0;width:700px;height:460px}
  .offer-tag{position:absolute;left:22px;top:10px;width:220px;color:var(--white);text-align:center;font-weight:800;line-height:1.05}
  .offer-tag .pct{display:block;font-size:40px;margin-top:18px}
  .offer-tag .pct small{font-size:24px}
  .offer-tag .note{display:block;font-size:15px;letter-spacing:.5px;margin-top:4px}
  .brand{position:absolute;right:40px;top:22px;display:flex;align-items:center;gap:10px;font-family:'Bebas Neue',sans-serif;font-size:44px;letter-spacing:2px;color:var(--red)}
  .brand .mark{width:18px;height:18px;background:var(--dark)}
  .title{position:absolute;left:0;right:30px;top:436px;text-align:right;font-family:'Bebas Neue',sans-serif;font-weight:400;line-height:.86}
  .title .lead{display:block;color:var(--red);font-size:72px;padding-right:170px}
  .title .main{display:block;color:var(--dark);font-size:98px}
  .gallery{position:absolute;left:24px;top:590px;display:flex;gap:10px}
  .gallery .shot{width:156px;height:108px;border:4px solid var(--white);box-shadow:0 3px 8px rgba(0,0,0,.3)}
  .shot.a{background:linear-gradient(180deg,#b9c4cf 0%,#8f959c 55%,#7c8a55 100%)}
  .shot.b{background:linear-gradient(180deg,#c7cdd3 0%,#a9a49a 55%,#8a7a5f 100%)}
  .shot.c{background:linear-gradient(180deg,#9fb3c9 0%,#d8cfb0 50%,#7c6a4e 100%)}
  .shot.d{background:linear-gradient(180deg,#a7b8c6 0%,#e2dccb 55%,#7b8655 100%)}
  .services{position:absolute;left:28px;top:718px;width:336px}
  .services h2,.about h2{font-size:18px;font-weight:800;color:var(--dark);text-transform:uppercase;line-height:1.2}
  .services h2 em,.about h2 em{font-style:normal;color:var(--red)}
  .service-list{display:flex;gap:14px;margin-top:8px;list-style:none}
  .service-list li{width:100px;text-align:center;font-size:12px;font-weight:600;line-height:1.25;color:var(--dark)}
  .service-list svg{display:block;margin:0 auto 4px}
  .about{position:absolute;left:376px;top:714px;width:300px}
  .about p{font-size:9.4px;line-height:1.45;margin-top:5px;color:var(--muted)}
  .estimate{position:absolute;left:30px;top:840px;font-size:22px;font-weight:600;color:var(--dark);line-height:1.2}
  .footer{position:absolute;left:0;bottom:0;width:700px;height:58px}
  .footer svg{position:absolute;left:0;top:0}
  .call{position:absolute;left:24px;top:6px;color:var(--white);font-family:'Bebas Neue',sans-serif;line-height:.9}
  .call .label{font-size:22px;letter-spacing:1px;display:block}
  .call .phone{font-size:38px;letter-spacing:2px}
  .contact{position:absolute;left:392px;top:14px;width:300px;color:var(--white);font-size:11.5px;line-height:1.35;letter-spacing:.3px}
  .contact strong{font-weight:800}
</style>
</head>
<body>
<main class="flyer">
  <section class="hero">
    <svg width="700" height="460" viewBox="0 0 700 460">
      <defs>
        <linearGradient id="photoTone" x1="0" y1="0" x2="0.3" y2="1">
          <stop offset="0" stop-color="#dfe5ea"/>
          <stop offset="0.35" stop-color="#8e8f8a"/>
          <stop offset="0.7" stop-color="#5f6466"/>
          <stop offset="1" stop-color="#6d7a55"/>
        </linearGradient>
      </defs>
      <polygon points="0,0 700,0 700,332 480,278 0,412" fill="url(#photoTone)" role="img" aria-label="Photo of a screened porch addition with gabled roof and dark screen panels"/>
      <path d="M470,0 H700 V76 H500 Q470,76 470,46 Z" fill="var(--white)"/>
      <polygon points="0,412 480,278 700,332 700,362 480,306 0,444" fill="var(--red)"/>
      <polygon points="0,444 480,306 700,362 700,374 480,320 0,458" fill="var(--dark)"/>
      <path d="M22,30 Q22,10 42,10 H242 V100 L132,132 L22,100 Z" fill="var(--red)"/>
    </svg>
    <div class="offer-tag">
      <span class="pct">10%<small>OFF</small></span>
      <span class="note">NEW GUTTER<br>INSTALLATION!</span>
    </div>
    <div class="brand"><span class="mark"></span>Crestway</div>
  </section>

  <h1 class="title"><span class="lead">Hillcrest</span><span class="main">Screen Porches</span></h1>

  <div class="gallery">
    <div class="shot a" role="img" aria-label="Project photo: gray screened porch beside a house"></div>
    <div class="shot b" role="img" aria-label="Project photo: white-framed screened porch on a deck"></div>
    <div class="shot c" role="img" aria-label="Project photo: yellow house with screened deck"></div>
    <div class="shot d" role="img" aria-label="Project photo: screened porch with white railing"></div>
  </div>

  <section class="services">
    <h2><em>Our</em> Services</h2>
    <ul class="service-list">
      <li>
        <svg width="44" height="44" viewBox="0 0 44 44"><circle cx="22" cy="22" r="20" fill="none" stroke="var(--red)" stroke-width="2"/><path d="M12 17h20v5H12z M20 22h4v10h-4z" fill="var(--red)"/></svg>
        Seamless Gutters
      </li>
      <li>
        <svg width="44" height="44" viewBox="0 0 44 44"><circle cx="22" cy="22" r="20" fill="none" stroke="var(--red)" stroke-width="2"/><path d="M11 15h22M14 15v5h16v-5M22 20v8" fill="none" stroke="var(--red)" stroke-width="2"/><circle cx="22" cy="31" r="2" fill="var(--red)"/></svg>
        Gutters &amp; Downspouts
      </li>
      <li>
        <svg width="44" height="44" viewBox="0 0 44 44"><circle cx="22" cy="22" r="20" fill="none" stroke="var(--red)" stroke-width="2"/><rect x="12" y="13" width="20" height="18" fill="none" stroke="var(--red)" stroke-width="2"/><path d="M22 13v18M12 22h20" stroke="var(--red)" stroke-width="1.5"/></svg>
        Screened in Porch
      </li>
    </ul>
  </section>

  <section class="about">
    <h2><em>Screen Porch</em> Enclosures</h2>
    <p>Adding a screened in porch to your home helps maximize the size of your lot by creating more habitable space. You will be able to utilize your new porch almost all year round, especially with the predictive warm weather patterns of Greenville &amp; Spartanburg, SC. A screened in porch is something future homebuyers will be looking for within these areas due to their functionality, this in turn increases the value of your home. Choosing the right home improvements to invest in now will help you get the most return on your property when you do decide to sell.</p>
  </section>

  <p class="estimate">For Free Estimate</p>

  <footer class="footer">
    <svg width="700" height="58" viewBox="0 0 700 58">
      <polygon points="0,0 340,0 380,58 0,58" fill="var(--red)"/>
      <polygon points="340,0 700,0 700,58 380,58" fill="var(--dark)"/>
    </svg>
    <div class="call"><span class="label">Call Us</span><span class="phone">864-555-0186</span></div>
    <p class="contact"><strong>DOM KARSTEN-</strong> 2957 Old Hwy 38 N, Greer, SC 29873</p>
  </footer>
</main>
</body>
</html>
```